Webdesign für Fliesenlegermeister
Zielgruppe
Baugewerbe. Platten und Fliesenlegermeister
Aufgabenstellung
Sollte modern wirken, jedoch nur eine Seite sein. Ich habe einen domain gekauft der derzeit offline ist und auch noch nie verwendet wurde.
domain wär: www.fliesenbergmoos-demo.at

```html
<!DOCTYPE html>
<html lang="de">
<head>
<meta charset="utf-8">
<title>Martin Bergmoser – Platten und Fliesenlegermeister</title>
<link rel="stylesheet" href="https://fonts.googleapis.com/css2?family=Oswald:wght@300;400;500&family=Roboto+Condensed:wght@300;400;700&display=swap">
<style>
  :root {
    --cyan: #00aeef;
    --navy: #0c4a73;
    --footer: #00507d;
    --text: #666a6e;
    --white: #ffffff;
    --rule: #eeeeee;
  }
  * { box-sizing: border-box; margin: 0; padding: 0; }
  html, body { width: 990px; height: 1200px; overflow: hidden; background: var(--white); }
  body { position: relative; font-family: "Roboto Condensed", Arial, sans-serif; color: var(--text); }

  .hero { position: absolute; left: 0; top: 0; width: 990px; height: 541px; overflow: hidden; }
  .hero-photo {
    position: absolute; inset: 0;
    background:
      linear-gradient(180deg, rgba(255,255,255,0) 0%, rgba(255,255,255,0) 55%, rgba(20,110,160,0.35) 100%),
      linear-gradient(90deg, #d7ecf6 0%, #8fc5e2 22%, #3d8fc0 50%, #6fb2d8 75%, #e4f2f9 100%);
  }
  .hero-cut { position: absolute; left: 0; top: 0; }
  .brand { position: absolute; left: 0; width: 990px; text-align: center; }
  .brand-top { top: 70px; }
  .brand-mark { display: block; width: 46px; height: 46px; margin: 0 auto 12px; background: var(--cyan); }
  .brand-name { font-family: "Oswald", sans-serif; font-weight: 500; font-size: 20px; letter-spacing: 0.5px; color: var(--navy); line-height: 1; }
  .brand-tag { font-family: "Oswald", sans-serif; font-weight: 300; font-size: 8.5px; letter-spacing: 1.6px; color: var(--cyan); margin-top: 4px; }

  .hero-title { position: absolute; top: 328px; width: 990px; text-align: center; font-family: "Oswald", sans-serif; font-weight: 500; font-size: 40px; letter-spacing: 1px; color: var(--white); line-height: 1; }
  .hero-sub { position: absolute; top: 378px; width: 990px; text-align: center; font-family: "Roboto Condensed", sans-serif; font-weight: 400; font-size: 13px; color: var(--white); }

  .service { position: absolute; top: 500px; width: 220px; text-align: center; }
  .service-badge { display: block; margin: 0 auto; }
  .service-title { margin-top: 18px; font-family: "Oswald", sans-serif; font-weight: 300; font-size: 12.5px; color: var(--navy); }
  .service-text { margin-top: 10px; font-size: 8.5px; line-height: 14px; }

  .divider { position: absolute; left: 193px; top: 700px; width: 604px; height: 1px; background: var(--rule); }

  .about { position: absolute; top: 748px; left: 180px; width: 630px; text-align: center; }
  .about-title { font-family: "Oswald", sans-serif; font-weight: 300; font-size: 24px; color: var(--cyan); line-height: 1; }
  .about p { font-size: 8.5px; line-height: 14.5px; margin-top: 14px; }
  .about p + p { margin-top: 14px; }

  .footer { position: absolute; left: 0; top: 942px; width: 990px; height: 258px; }
  .footer-shape { position: absolute; left: 0; top: 0; }
  .footer .brand { top: 34px; }
  .footer .brand-mark { width: 40px; height: 40px; background: var(--cyan); margin-bottom: 10px; }
  .footer .brand-name { color: var(--white); font-size: 15px; }
  .footer .brand-tag { font-size: 7px; }
  .contact { position: absolute; top: 130px; width: 990px; text-align: center; font-family: "Oswald", sans-serif; font-weight: 300; font-size: 14px; letter-spacing: 2.2px; color: var(--white); line-height: 17px; }
  .contact-group + .contact-group { margin-top: 6px; }
  .contact-web { color: var(--cyan); }
</style>
</head>
<body>
  <header class="hero">
    <div class="hero-photo" role="img" aria-label="Foto eines hellen Flurs mit glänzendem Granitboden, großen Fenstern und Pflanzen, in Blautönen"></div>
    <svg class="hero-cut" width="990" height="541" viewBox="0 0 990 541" aria-hidden="true">
      <polygon points="258,0 729,0 495,217" fill="#ffffff"/>
    </svg>
    <div class="brand brand-top">
      <span class="brand-mark"></span>
      <div class="brand-name">MARTIN BERGMOSER</div>
      <div class="brand-tag">PLATTEN UND FLIESENLEGERMEISTER</div>
    </div>
    <h1 class="hero-title">LOREM IPSUM</h1>
    <div class="hero-sub">DONEC A LECTUS NON PURUS ULTRICIES ELEIFEND</div>
  </header>

  <section class="services">
    <div class="service" style="left:171px">
    <svg class="service-badge" width="82" height="82" viewBox="0 0 82 82" aria-hidden="true">
      <rect x="17" y="17" width="48" height="48" transform="rotate(45 41 41)" fill="#00aeef" stroke="#ffffff" stroke-width="3"/>
      <g fill="none" stroke="#ffffff" stroke-width="1.2" stroke-linecap="round">
        <path d="M31 31 l4 -2 l4 4 l-2 4 l14 14 l-3 3 l-14 -14 l-4 2 l-4 -4 z"/>
        <path d="M49 30 l3 3 l-16 16 l-3 1 l1 -3 z"/>
        <circle cx="49" cy="49" r="3"/>
      </g>
    </svg>
      <div class="service-title">LOREM IPSUM DOLOR</div>
      <div class="service-text">Lorem ipsum dolor sit amet, consectetur adipi<br>elit. Nulla lobortis consequat mauris</div>
    </div>
    <div class="service" style="left:385px">
    <svg class="service-badge" width="82" height="82" viewBox="0 0 82 82" aria-hidden="true">
      <rect x="17" y="17" width="48" height="48" transform="rotate(45 41 41)" fill="#00aeef" stroke="#ffffff" stroke-width="3"/>
      <g fill="none" stroke="#ffffff" stroke-width="1.2">
        <rect x="29" y="29" width="24" height="24" rx="2"/>
        <rect x="32" y="32" width="8" height="8" rx="1"/>
        <rect x="42" y="32" width="8" height="8" rx="1"/>
        <rect x="32" y="42" width="8" height="8" rx="1"/>
        <rect x="42" y="42" width="8" height="8" rx="1"/>
      </g>
    </svg>
      <div class="service-title">LOREM IPSUM DOLOR</div>
      <div class="service-text">Lorem ipsum dolor sit amet, consectetur adipi<br>elit. Nulla lobortis consequat mauris</div>
    </div>
    <div class="service" style="left:601px">
    <svg class="service-badge" width="82" height="82" viewBox="0 0 82 82" aria-hidden="true">
      <rect x="17" y="17" width="48" height="48" transform="rotate(45 41 41)" fill="#00aeef" stroke="#ffffff" stroke-width="3"/>
      <g fill="none" stroke="#ffffff" stroke-width="1.2" stroke-linecap="round">
        <circle cx="43" cy="39" r="8"/>
        <path d="M33 35 c-3 4 -2 10 3 14 c3 2 6 3 9 2 l-2 -4 l-3 1 c-3 -2 -5 -5 -5 -8 l2 -2 z"/>
      </g>
      <text x="43" y="42" text-anchor="middle" font-family="Roboto Condensed, sans-serif" font-size="7" fill="#ffffff">24</text>
    </svg>
      <div class="service-title">LOREM IPSUM DOLOR</div>
      <div class="service-text">Lorem ipsum dolor sit amet, consectetur adipi<br>elit. Nulla lobortis consequat mauris</div>
    </div>
  </section>

  <div class="divider"></div>

  <section class="about">
    <h2 class="about-title">ÜBER MICH</h2>
    <p>Lorem ipsum dolor sit amet, consectetur adipiscing elit. Nulla lobortis consequat mauris, eget eleifend nunc viverra viverra. Ut ac risus odio. Aliquam pretium purus sed nulla feugiat blandit. Cras vel libero ut lacus eleifend tempor phasellus eleifend.</p>
    <p>Magna non tincidunt accumsan, justo arcu cursus ipsum, non porttitor sapien quam vel magna. Maecenas elit nisl, molestie nec dapibus nec, aliquet a erat. Donec scelerisque lacus a libero suscipit auctor volutpat enim euismod. Mauris porta, lacus ut ullamcorper sodales, mauris tortor feugiat purus, nec aliquam neque purus ac metus. Nunc eleifend leo quis nisl hendrerit ultrices. Suspendisse quis feugiat elit. Fusce vitae dolor ac est tincidunt feugiat. Phasellus volutpat dui in sapien malesuada tempus placerat justo ultricies. Duis mollis ornare risus, ut consectetur mi tincidunt sit amet.</p>
  </section>

  <footer class="footer">
    <svg class="footer-shape" width="990" height="258" viewBox="0 0 990 258" aria-hidden="true">
      <polygon points="0,23 447,23 495,0 543,23 990,23 990,258 0,258" fill="#00507d"/>
    </svg>
    <div class="brand">
      <span class="brand-mark"></span>
      <div class="brand-name">MARTIN BERGMOSER</div>
      <div class="brand-tag">PLATTEN UND FLIESENLEGERMEISTER</div>
    </div>
    <address class="contact" style="font-style:normal">
      <div class="contact-group">MARTIN BERGMOSER<br>LINDENWEG 12 | 5100 TALHEIM</div>
      <div class="contact-group">TEL.: 0660 123 45 67<br>MAIL: FLIESEN-BERGMOOS@DEMO.AT</div>
      <div class="contact-group contact-web">WWW.FLIESENBERGMOOS-DEMO.AT</div>
    </address>
  </footer>
</body>
</html>
```